Hot Yoga Studio

We need a wordpress design for a new hot yoga studio. We will offer the Dravel yoga sequence, Corvelle power yoga sequence, gentle hatha, vinyasa flow, kids yoga, family yoga, prenatal and postnatal yoga, etc.

We offer a very wide variety of heated and non-heated classes. We would like for our studio to feel like an oasis that yogis can escape to. Calming, refreshing, restorative, renewal, relax, replenish, revive are all words we connect with our brand. We would like to see designs that utilize blues and greens and connect with our logo.

The final design should communicate a place to develop a strong able body and clear quiet mind. A place to eliminate stress and get away … very spa-like.

We like the organization of StillGrove website. We understand our organization will have to be a bit different because Stillgrove has many locations. But, overall we like the flow and organization of their site.

Target Market(s)

women, mothers, sports teams

Font styles to use
Serif
Sans Serif

Colors
00a990
34b8a5
86cfc6
d0ebe7
0892cd
33a6d7
85cae6
cee9f5

Requirements
Must have
• SCHEDULE link - must be easy to find on home page

```html
<!DOCTYPE html>
<html lang="en">
<head>
<meta charset="utf-8">
<title>Lumen Hot Yoga Studio</title>
<link rel="stylesheet" href="https://fonts.googleapis.com/css2?family=Arimo:wght@400;700&display=swap">
<style>
:root{
  --blue:#33a6d7;
  --blue-deep:#0892cd;
  --banner:#2fa3d6;
  --teal:#34b8a5;
  --ink:#555;
  --muted:#888;
  --rule:#e2e2e2;
  --footer:#f4f4f4;
  --white:#fff;
}
*{margin:0;padding:0;box-sizing:border-box}
html,body{width:1200px;height:1000px;overflow:hidden;background:var(--white)}
body{position:relative;font-family:"Arimo",Arial,sans-serif;color:var(--ink)}
h1,h2,h3,h4{font-weight:400}
a{text-decoration:none}
.abs{position:absolute}
.brand{display:flex;align-items:center;gap:6px;font-size:22px;letter-spacing:1px;color:var(--teal);font-weight:400}
.brand-dot{width:14px;height:14px;border-radius:50%;background:var(--teal)}
.nav{top:57px;left:595px;font-size:7px;color:var(--ink)}
.nav a{color:inherit;position:absolute;white-space:nowrap}
.nav a.active{color:var(--blue)}
.hero{left:390px;top:79px;width:428px;height:203px;background:linear-gradient(180deg,#4f8ea8 0%,#6fb0c9 55%,#3f7f99 100%)}
.hero-figure{position:absolute;right:0;top:0;width:200px;height:203px;background:linear-gradient(90deg,rgba(30,80,105,0) 0%,rgba(25,75,100,.55) 60%,rgba(25,75,100,.4) 100%)}
.hero-brand{position:absolute;left:46px;top:62px;display:flex;align-items:center;gap:4px;font-size:14px;letter-spacing:1px;color:var(--white)}
.hero-brand .brand-dot{width:9px;height:9px;background:var(--white)}
.hero-copy{position:absolute;left:46px;top:89px;width:160px;font-size:7px;line-height:10px;color:var(--white)}
.section-title{left:390px;width:428px;display:flex;align-items:center;gap:12px;font-size:13px;color:var(--blue);white-space:nowrap}
.section-title::before,.section-title::after{content:"";flex:1;height:1px;background:var(--rule)}
.tile{top:332px;width:104px;height:71px}
.tile-overlay{background:rgba(51,166,215,.85);color:var(--white);text-align:center;font-size:6px;padding-top:28px}
.tile-overlay small{display:block;font-size:4.5px;margin-top:6px;letter-spacing:.3px}
.banner{left:390px;top:426px;width:428px;height:166px;background:var(--banner)}
.banner-figure{position:absolute;left:10px;top:8px;width:140px;height:150px;background:linear-gradient(180deg,#4db3e0,#2a93c4)}
.banner-title{position:absolute;left:157px;top:37px;font-size:20px;color:var(--white)}
.banner-copy{position:absolute;left:157px;top:65px;width:264px;font-size:6.5px;line-height:8px;color:var(--white)}
.banner-link{position:absolute;left:158px;top:115px;font-size:7px;color:var(--white)}
.card-title{top:757px;font-size:10px;color:#666;text-transform:uppercase;white-space:nowrap}
.card-copy{top:775px;font-size:6.2px;line-height:9px;color:var(--muted)}
.link{font-size:6.3px;color:var(--blue);text-transform:uppercase}
.footer{left:390px;top:835px;width:428px;height:165px;background:var(--footer)}
.footer .brand{position:absolute;left:18px;top:24px;color:#9a9a9a;font-size:20px}
.footer .brand-dot{background:#9a9a9a;width:12px;height:12px}
.footer-about{position:absolute;left:18px;top:64px;width:160px;font-size:5.5px;line-height:8px;color:var(--muted)}
.footer-head{position:absolute;top:24px;font-size:9px;color:var(--blue)}
.footer-rule{position:absolute;top:40px;height:1px;background:#e0e0e0}
.footer-links{position:absolute;left:210px;top:48px;list-style:none;font-size:6px;line-height:10.3px;color:#666}
.footer-links .active{color:var(--blue)}
.contact-name{position:absolute;left:309px;top:48px;font-size:7px;color:#777}
.contact-row{position:absolute;left:309px;font-size:5.5px;color:var(--muted);display:flex;align-items:center;gap:8px;white-space:nowrap}
.contact-row svg{width:6px;height:6px;fill:#777}
.footer-divider{position:absolute;left:18px;top:127px;width:388px;height:1px;background:#e0e0e0}
.copyright{position:absolute;left:18px;top:140px;font-size:5.3px;color:var(--muted)}
.copyright .hl{color:var(--blue)}
</style>
</head>
<body>

<header>
  <div class="abs brand" style="left:392px;top:38px"><span class="brand-dot"></span>LUMEN</div>
  <nav class="abs nav">
    <a class="active" style="left:0">Home</a>
    <a style="left:38px">About Us</a>
    <a style="left:82px">Training</a>
    <a style="left:122px">Courses</a>
    <a style="left:162px">Blogs</a>
    <a style="left:191px">Contact Us</a>
  </nav>
</header>

<section class="abs hero" role="img" aria-label="Photo of a woman meditating in lotus pose by the sea, tinted blue">
  <div class="hero-figure"></div>
  <div class="hero-brand"><span class="brand-dot"></span>LUMEN</div>
  <p class="hero-copy">Ut wisi enim ad minim veniam, quis nostrud exerci tation ullamcorper suscipit lobortis nisl ut aliquip ex ea commodo consequat.</p>
</section>

<h2 class="abs section-title" style="top:299px">OUR CORE FEATURES</h2>

<div class="abs tile" style="left:390px;background:linear-gradient(180deg,#6f9a3a,#9bbf4a 60%,#c9c93a)" role="img" aria-label="Photo of a woman in a yoga pose on grass"></div>
<div class="abs tile tile-overlay" style="left:498px" role="img" aria-label="Photo of a yoga pose with hover overlay">Lorem Ipsum is simply dummy text<small>LEARN MORE</small></div>
<div class="abs tile" style="left:606px;background:linear-gradient(180deg,#6f9a3a,#9bbf4a 60%,#c9c93a)" role="img" aria-label="Photo of a woman in a yoga pose on grass"></div>
<div class="abs tile" style="left:714px;background:linear-gradient(180deg,#cfd6dc,#8a949c 70%,#2c3338)" role="img" aria-label="Silhouette of a dancer pose against the sky"></div>

<section class="abs banner">
  <div class="banner-figure" role="img" aria-label="Photo of a woman in a king pigeon yoga pose"></div>
  <h2 class="banner-title">Lorem ipsum dolor sit!</h2>
  <p class="banner-copy">aliquam erat volutpat. Ut wisi enim ad minim veniam, quis nostrud exerci tation ullamcorper suscipit lobortis nisl ut aliquip ex ea commodo consequat.</p>
  <a class="banner-link">LEARN MORE &gt;</a>
</section>

<h2 class="abs section-title" style="top:611px">HEADING LOREM IP</h2>

<div class="abs" style="left:390px;top:642px;width:256px;height:102px;background:linear-gradient(180deg,#f0a21e,#f7c53a 55%,#d98a10)" role="img" aria-label="Silhouette of a woman in warrior pose at sunset on the beach"></div>
<h3 class="abs card-title" style="left:390px">Lorem Ipsum is simply dummy text</h3>
<p class="abs card-copy" style="left:390px;width:262px">Lorem Ipsum is simply dummy text of the printing and typesetting industry. Lorem Ipsum has been the industry's standard dummy</p>
<a class="abs link" style="left:390px;top:801px">Learn more</a>

<div class="abs" style="left:657px;top:642px;width:161px;height:102px;background:linear-gradient(180deg,#6f9a3a,#a8c46a 60%,#7a6548)" role="img" aria-label="Photo of a woman meditating on a wooden bridge"></div>
<h3 class="abs card-title" style="left:657px">Lorem Ipsum is simply</h3>
<p class="abs card-copy" style="left:657px;width:166px">Lorem Ipsum is simply dummy text of the printing and typesetting industry</p>
<a class="abs link" style="left:657px;top:801px">Learn more</a>

<footer class="abs footer">
  <div class="brand"><span class="brand-dot"></span>LUMEN</div>
  <p class="footer-about">Lorem Ipsum is simply dummy text of the printing and typeset­ting industry. Lorem Ipsum has been the industry's standard dummy text ever since the 1500s, when an unknown</p>
  <a class="abs link" style="left:18px;top:101px;font-size:5.6px">Learn more</a>

  <h4 class="footer-head" style="left:210px">Site Links</h4>
  <div class="footer-rule" style="left:210px;width:56px"></div>
  <ul class="footer-links">
    <li>Home</li><li>About Us</li><li class="active">Training</li><li>Courses</li><li>Blogs</li><li>Contact Us</li>
  </ul>

  <h4 class="footer-head" style="left:309px">Contact Info</h4>
  <div class="footer-rule" style="left:309px;width:96px"></div>
  <p class="contact-name">Lumen Hot Yoga Studio</p>
  <div class="contact-row" style="top:63px"><svg viewBox="0 0 10 10"><path d="M5 0a3.5 3.5 0 0 0-3.5 3.5C1.5 6 5 10 5 10s3.5-4 3.5-6.5A3.5 3.5 0 0 0 5 0zm0 5a1.5 1.5 0 1 1 0-3 1.5 1.5 0 0 1 0 3z"/></svg>#123 Street Name, City State 1234</div>
  <div class="contact-row" style="top:73px"><svg viewBox="0 0 10 10"><path d="M2 0l2 2.5-1 1.2a6 6 0 0 0 3.3 3.3l1.2-1L10 8l-1.5 2C4 10 0 6 0 1.5z"/></svg>123 456 78900</div>
  <div class="contact-row" style="top:83px"><svg viewBox="0 0 10 10"><path d="M0 2h10v6H0z"/></svg>info@example.com</div>
  <div class="contact-row" style="top:93px"><svg viewBox="0 0 10 10"><circle cx="5" cy="5" r="4.5" fill="none" stroke="#777"/><path d="M1 5h8M5 .5v9" stroke="#777" fill="none"/></svg>www.lumenyoga.example</div>

  <div class="footer-divider"></div>
  <p class="copyright">Copyright © 2014 Company Name. &nbsp;All Rights Reserved. &nbsp;| &nbsp;<span class="hl">Privacy Policy</span> &nbsp;| &nbsp;Terms &amp; Condition</p>
</footer>

</body>
</html>
```